Brevolt custom business card design

After a business card incorporating the attached logo, I want the following

Brevolt
-Aluminium Windows & doors
-cladding
-roof access systems
-labour hire
-disabled access audits and alterations
-general carpentry

F 7, 21 wren gully road, Kestrelton 3991
Ph: 5937 2418
Fax: 5937 2451
Mob: 0400 731 946
Marcus@brevoltworks.example

Target Market(s)

Construction industry

Industry/Entity Type

Business

Contact Information for Business Card

As per brief

Font styles to use
Serif
Script

```html
<!DOCTYPE html>
<html lang="en">
<head>
<meta charset="utf-8">
<title>Brevolt business card</title>
<link rel="stylesheet" href="https://fonts.googleapis.com/css2?family=PT+Sans:wght@400;700&display=swap">
<style>
  :root {
    --bg: #e6e4e0;
    --card-black: #0b0b0c;
    --card-white: #f2f2f2;
    --navy: #1b2a78;
    --orange: #f0661c;
    --gold: #f1b21f;
    --ink: #2b2b2b;
    --ink-soft: #555555;
    --sep: #cfcfcf;
  }
  * { box-sizing: border-box; margin: 0; padding: 0; }
  html, body { width: 1200px; height: 900px; overflow: hidden; }
  body {
    background: var(--bg);
    font-family: "PT Sans", sans-serif;
    display: flex;
    flex-direction: column;
    align-items: center;
    justify-content: center;
    gap: 44px;
  }
  .card {
    position: relative;
    width: 640px;
    height: 390px;
    border-radius: 28px;
    overflow: hidden;
    background: var(--card-white);
    box-shadow: 0 10px 28px rgba(0,0,0,0.22);
  }
  .card-bg { position: absolute; inset: 0; width: 100%; height: 100%; }
  .wordmark {
    position: absolute;
    font-weight: 700;
    letter-spacing: 0.5px;
    display: flex;
    align-items: center;
    gap: 12px;
    line-height: 1;
  }
  .wordmark-dot { border-radius: 50%; display: inline-block; }

  /* Contact side */
  .card-contact .wordmark { left: 40px; top: 26px; font-size: 44px; color: #ffffff; }
  .card-contact .wordmark-dot { width: 16px; height: 16px; background: #ffffff; }
  .person { position: absolute; right: 46px; top: 146px; text-align: right; }
  .person-name { font-size: 21px; font-weight: 700; color: var(--ink); line-height: 1.2; }
  .person-role { font-size: 15px; color: var(--ink-soft); line-height: 1.2; }
  .contact-list {
    position: absolute; left: 46px; top: 196px;
    list-style: none; display: flex; flex-direction: column; gap: 5px;
  }
  .contact-list li {
    display: flex; align-items: center; gap: 10px;
    font-size: 18px; line-height: 1.2; color: var(--ink);
  }
  .contact-list svg { width: 16px; height: 16px; flex: none; }

  /* Services side */
  .card-services .wordmark {
    left: 0; right: 0; top: 70px; justify-content: center;
    font-size: 92px; color: var(--navy);
  }
  .card-services .wordmark-dot { width: 30px; height: 30px; background: var(--navy); }
  .services {
    position: absolute; left: 0; right: 0; top: 240px;
    text-align: center; color: var(--orange);
    font-size: 21px; line-height: 1.3;
  }
  .services .sep { color: var(--sep); padding: 0 2px; }
  .website {
    position: absolute; left: 0; right: 0; top: 336px;
    text-align: center; color: var(--gold); font-size: 19px; line-height: 1.2;
  }
</style>
</head>
<body>

  <section class="card card-contact" aria-label="Business card, contact side">
    <svg class="card-bg" viewBox="0 0 640 390" preserveAspectRatio="none" aria-hidden="true">
      <rect width="640" height="390" fill="var(--card-white)"/>
      <polygon points="0,0 640,0 640,72 0,102" fill="var(--card-black)"/>
    </svg>
    <div class="wordmark"><span class="wordmark-dot"></span>Brevolt</div>
    <div class="person">
      <p class="person-name">Marcus Hollin</p>
      <p class="person-role">President</p>
    </div>
    <ul class="contact-list">
      <li>
        <svg viewBox="0 0 16 16" aria-hidden="true"><path d="M8 1a5 5 0 0 0-5 5c0 3.6 5 9 5 9s5-5.4 5-9a5 5 0 0 0-5-5zm0 7a2 2 0 1 1 0-4 2 2 0 0 1 0 4z" fill="var(--orange)"/></svg>
        F 7, 21 Wren Gully Road, Kestrelton 3991
      </li>
      <li>
        <svg viewBox="0 0 16 16" aria-hidden="true"><circle cx="8" cy="8" r="7" fill="var(--orange)"/><path d="M5.5 4.5l1.5 1.5-1 1a5 5 0 0 0 3 3l1-1 1.5 1.5-1.2 1.2C7.5 11.6 4.4 8.5 4.3 5.7z" fill="#fff"/></svg>
        5937 2418
      </li>
      <li>
        <svg viewBox="0 0 16 16" aria-hidden="true"><rect x="4" y="1.5" width="8" height="5" fill="var(--orange)"/><rect x="1" y="6" width="14" height="6" rx="1.5" fill="var(--orange)"/><rect x="4" y="10" width="8" height="4.5" fill="var(--orange)" stroke="#fff" stroke-width="1"/></svg>
        5937 2451
      </li>
      <li>
        <svg viewBox="0 0 16 16" aria-hidden="true"><rect x="4" y="1" width="8" height="14" rx="1.5" fill="var(--orange)"/><rect x="5.5" y="3" width="5" height="8" fill="#fff"/><circle cx="8" cy="13" r="0.9" fill="#fff"/></svg>
        0400 731 946
      </li>
      <li>
        <svg viewBox="0 0 16 16" aria-hidden="true"><rect x="1" y="3" width="14" height="10" rx="1" fill="var(--orange)"/><path d="M1.5 3.5L8 9l6.5-5.5" fill="none" stroke="#fff" stroke-width="1.2"/></svg>
        Marcus@brevoltworks.example
      </li>
    </ul>
  </section>

  <section class="card card-services" aria-label="Business card, services side">
    <svg class="card-bg" viewBox="0 0 640 390" preserveAspectRatio="none" aria-hidden="true">
      <rect width="640" height="390" fill="var(--card-white)"/>
      <polygon points="0,232 640,190 640,390 0,390" fill="var(--card-black)"/>
    </svg>
    <div class="wordmark"><span class="wordmark-dot"></span>Brevolt</div>
    <p class="services">
      Aluminium windows &amp; doors <span class="sep">|</span> Cladding <span class="sep">|</span> Roof access systems<br>
      Labour hire <span class="sep">|</span> Disabled access audits and alterations<br>
      General carpentry
    </p>
    <p class="website">www.brevoltworks.example</p>
  </section>

</body>
</html>
```